Harborline Crest Insurance Services

we are a high end insurance agency we specialize on Auto | Home | Business | Life looking for something professional and luxuries at the same time. if you guys need anything else please let me know.

Auto | Home | Business | Life must be under logo on the back with black background.

i want the back part to be black with our gold logo on it.

Target Market(s)

Auto | Home | Business | Life

Industry/Entity Type

Insurance Broker

Contact Information for Business Card

My logo is gold so a black in the back would be nice.

Font styles to use
Serif

Colors
000000

Requirements
Must have
• Big logo on the back with black background.

```html
<!DOCTYPE html>
<html lang="en">
<head>
<meta charset="utf-8">
<title>Harborline Crest Insurance Services – Business Card</title>
<link rel="stylesheet" href="https://fonts.googleapis.com/css2?family=Open+Sans:wght@400;600&display=swap">
<style>
  :root {
    --backdrop: #dcdcdc;
    --card-black: #000000;
    --card-white: #ffffff;
    --gold: #f2c318;
    --grey-text: #8c8c8c;
    --ink: #2b2b2b;
    --body-text: #555555;
    --icon: #777777;
    --divider: #cfcfcf;
  }
  * { box-sizing: border-box; margin: 0; padding: 0; }
  html, body {
    width: 1200px; height: 1000px; overflow: hidden;
    background: var(--backdrop);
    font-family: "Open Sans", Arial, sans-serif;
  }
  .stage {
    width: 1200px; height: 1000px;
    display: flex; align-items: center; justify-content: center; gap: 50px;
  }
  .card {
    position: relative; width: 540px; height: 320px;
    border-radius: 32px; overflow: hidden;
    box-shadow: 0 10px 24px rgba(0,0,0,0.18);
  }

  /* Brand placeholder: plain name with one plain circle */
  .brand {
    display: flex; align-items: center; gap: 14px;
  }
  .brand-mark {
    flex: none; border-radius: 50%; background: var(--gold);
  }
  .brand-name {
    font-weight: 600; color: var(--gold); line-height: 1.25;
  }

  /* Logo side */
  .card--back {
    background: var(--card-black);
    display: flex; flex-direction: column; align-items: center; justify-content: center; gap: 22px;
  }
  .card--back .brand { flex-direction: column; gap: 14px; }
  .card--back .brand-mark { width: 64px; height: 64px; }
  .card--back .brand-name { font-size: 24px; text-align: center; }
  .services {
    font-size: 14px; letter-spacing: 2px; color: var(--grey-text); text-transform: uppercase;
  }
  .services .sep { color: var(--gold); margin: 0 6px; }

  /* Contact side */
  .card--front { background: var(--card-white); }
  .front-band {
    position: absolute; left: 0; top: 0; width: 100%; height: 180px;
    background: var(--card-black);
    display: flex; align-items: center; padding-left: 40px;
  }
  .front-band .brand-mark { width: 48px; height: 48px; }
  .front-band .brand-name { font-size: 19px; }
  .holder { position: absolute; left: 40px; top: 212px; }
  .holder-name { font-size: 28px; font-weight: 600; color: var(--ink); line-height: 1.3; }
  .holder-name .surname { color: var(--gold); }
  .holder-role { font-size: 15px; font-weight: 600; color: var(--grey-text); }
  .divider {
    position: absolute; left: 280px; top: 196px; width: 1px; height: 106px;
    background: var(--divider);
  }
  .contact {
    position: absolute; left: 302px; top: 196px;
    font-size: 12.5px; color: var(--body-text); line-height: 1.6; list-style: none;
  }
  .contact li { display: flex; align-items: center; gap: 8px; }
  .contact .icon { width: 11px; height: 11px; fill: var(--icon); flex: none; }
  .contact .address { padding-left: 19px; }
</style>
</head>
<body>
<main class="stage">
  <section class="card card--back" aria-label="Card back">
    <div class="brand">
      <span class="brand-mark"></span>
      <p class="brand-name">Harborline Crest<br>Insurance Services</p>
    </div>
    <p class="services">Auto<span class="sep">|</span>Home<span class="sep">|</span>Business<span class="sep">|</span>Life</p>
  </section>

  <section class="card card--front" aria-label="Card front">
    <div class="front-band">
      <div class="brand">
        <span class="brand-mark"></span>
        <p class="brand-name">Harborline Crest<br>Insurance Services</p>
      </div>
    </div>
    <div class="holder">
      <p class="holder-name">Daniel <span class="surname">Reyes</span></p>
      <p class="holder-role">Ceo &amp; Founder</p>
    </div>
    <div class="divider"></div>
    <ul class="contact">
      <li class="address">Your Street Address</li>
      <li class="address">Portmere, 1234</li>
      <li><svg class="icon" viewBox="0 0 24 24"><path d="M6.6 10.8a15 15 0 0 0 6.6 6.6l2.2-2.2c.3-.3.7-.4 1-.2 1.1.4 2.3.6 3.6.6.6 0 1 .4 1 1V20c0 .6-.4 1-1 1A17 17 0 0 1 3 4c0-.6.4-1 1-1h3.5c.6 0 1 .4 1 1 0 1.3.2 2.5.6 3.6.1.3 0 .7-.2 1z"/></svg>+000 12345 6789</li>
      <li><svg class="icon" viewBox="0 0 24 24"><path d="M2 5h20v14H2z M2 5l10 8 10-8" fill="none" stroke="#777" stroke-width="2"/></svg>yourname@email.com</li>
      <li><svg class="icon" viewBox="0 0 24 24"><circle cx="12" cy="12" r="10" fill="none" stroke="#777" stroke-width="2"/><path d="M2 12h20M12 2c3 3 3 17 0 20M12 2c-3 3-3 17 0 20" fill="none" stroke="#777" stroke-width="2"/></svg>www.youwebsitename.com</li>
    </ul>
  </section>
</main>
</body>
</html>
```